I require a set of preaching screens for our Easter weekend.

1. Good Friday Service Title: Still Lanterns
2. Easter Sunday Service Title Bright Harbor
3. Message Title Screen Title Bright Harbor
Overview
We need a set of clean, minimal screen graphics for 3 service sermon series called Bright Harbor
All screens must be delivered at 1920x1080px (16:9), suitable for projection in a church auditorium.

Design style
Minimal and clean. Uncluttered. Strong typography. Subtle use of imagery or texture — nothing busy or overly decorative.

The tone should feel thoughtful and weighty without being dark or heavy.

Subtitle: Letters Written Beside a Quiet Harbor Gate
Date range: 1 March – 5 April

Branding
No existing branding to match. Designer has creative freedom on colour palette and typography, provided the overall feel remains minimal and clean.
What to avoid
Busy backgrounds or heavy textures
All files in PNG at 1920x1080px
Editable source files (PSD or AI)

Please use images below as you feel is appropriate - we have permission for these - We want to see a at least three options for these screens to .

We need designs within 3 days

```html
<!DOCTYPE html>
<html lang="en">
<head>
<meta charset="utf-8">
<title>Bright Harbor – Screen Options</title>
<link rel="stylesheet" href="https://fonts.googleapis.com/css2?family=Outfit:wght@300;400;500;600&family=Playfair+Display:ital,wght@0,400;1,400;1,500&family=Oswald:wght@500&display=swap">
<style>
  :root {
    --page: #ffffff;
    --navy: #1b2c52;
    --gold: #d9b45f;
    --gold-soft: #c9a553;
  }
  * { margin: 0; padding: 0; box-sizing: border-box; }
  html, body { width: 712px; height: 1200px; overflow: hidden; background: var(--page); }
  .sheet { position: relative; width: 712px; height: 1200px; }

  .screen {
    position: absolute; left: 12px; width: 688px; height: 386px;
    background: var(--navy); overflow: hidden; color: var(--gold);
  }
  .screen--script { top: 11px; }
  .screen--seal { top: 407px; }
  .screen--modern { top: 803px; }

  /* Option 1 – script title */
  .rule { position: absolute; height: 1px; background: var(--gold-soft); opacity: .7; }
  .screen--script .rule--left { left: 124px; width: 64px; top: 165px; }
  .screen--script .rule--right { left: 499px; width: 66px; top: 165px; }
  .crown-art {
    position: absolute; left: 194px; top: 75px; width: 91px; height: 62px;
    background: linear-gradient(180deg, #e0bd68, #c49d4c); border-radius: 6px; opacity: .9;
  }
  .script-title {
    position: absolute; font-family: "Playfair Display", serif; font-style: italic;
    font-weight: 500; font-size: 80px; line-height: 80px; white-space: nowrap;
  }
  .script-title--first { left: 288px; top: 102px; }
  .script-title--second { left: 203px; top: 168px; }
  .script-subtitle {
    position: absolute; left: 0; right: 0; top: 283px; text-align: center;
    font-family: "Outfit", sans-serif; font-weight: 400; font-size: 16px; letter-spacing: .4px;
  }
  .script-dates {
    position: absolute; left: 0; right: 0; top: 310px; text-align: center;
    font-family: "Outfit", sans-serif; font-weight: 300; font-size: 15px; letter-spacing: .6px;
  }

  /* Option 2 – seal */
  .seal { position: absolute; inset: 0; }
  .seal-serif { font-family: "Playfair Display", serif; fill: var(--gold); }
  .seal-letter { font-family: "Oswald", sans-serif; font-weight: 500; font-size: 27px; fill: var(--gold); }

  /* Option 3 – modern */
  .modern-title {
    position: absolute; left: 0; right: 0; top: 84px; text-align: center;
    font-family: "Outfit", sans-serif; font-weight: 500; font-size: 52px; letter-spacing: -2px; line-height: 60px;
  }
  .modern-subtitle {
    position: absolute; left: 0; right: 0; top: 155px; text-align: center;
    font-family: "Outfit", sans-serif; font-weight: 300; font-size: 15.5px; letter-spacing: -.2px;
  }
  .cross-mark { position: absolute; left: 322px; top: 205px; }
  .modern-dates {
    position: absolute; left: 0; right: 0; top: 278px; text-align: center;
    font-family: "Outfit", sans-serif; font-weight: 600; font-size: 15px; letter-spacing: -.3px;
  }
</style>
</head>
<body>
<main class="sheet">

  <section class="screen screen--script">
    <div class="rule rule--left"></div>
    <div class="rule rule--right"></div>
    <div class="crown-art" role="img" aria-label="Engraved gold crown illustration"></div>
    <h1 class="script-title script-title--first">Bright</h1>
    <h1 class="script-title script-title--second">Harbor</h1>
    <p class="script-subtitle">Letters Written Beside a Quiet Harbor Gate</p>
    <p class="script-dates">1 MARCH- 5 APRIL</p>
  </section>

  <section class="screen screen--seal">
    <svg class="seal" width="688" height="386" viewBox="0 0 688 386">
      <defs>
        <path id="seal-baseline" d="M 222 196 A 122 122 0 0 0 466 196"/>
      </defs>
      <line x1="39" y1="196" x2="126" y2="196" stroke="var(--gold-soft)" stroke-width="1" opacity=".7"/>
      <line x1="555" y1="196" x2="642" y2="196" stroke="var(--gold-soft)" stroke-width="1" opacity=".7"/>
      <path d="M 223.3 228.4 A 125 125 0 1 1 464.7 228.4" fill="none" stroke="var(--gold)" stroke-width="0.9"/>
      <text class="seal-serif" x="138" y="202" font-size="15" text-anchor="start">1 MARCH</text>
      <text class="seal-serif" x="481" y="202" font-size="15" text-anchor="start">5 APRIL</text>
      <text class="seal-serif" x="344" y="121" font-size="17" font-style="italic" text-anchor="middle">BRIGHT</text>
      <text class="seal-letter" x="280" y="172" text-anchor="middle">H</text>
      <text class="seal-letter" x="307" y="161" text-anchor="middle">A</text>
      <text class="seal-letter" x="333" y="153" text-anchor="middle">R</text>
      <text class="seal-letter" x="359" y="153" text-anchor="middle">B</text>
      <text class="seal-letter" x="385" y="161" text-anchor="middle">O</text>
      <text class="seal-letter" x="411" y="172" text-anchor="middle">R</text>
      <rect x="262" y="184" width="164" height="90" rx="8" fill="var(--gold)" opacity=".88" role="img" aria-label="Engraved gold crown illustration"/>
      <text class="seal-serif" font-size="13" font-style="italic" letter-spacing=".3">
        <textPath href="#seal-baseline" startOffset="50%" text-anchor="middle">Letters Written Beside a Quiet Harbor Gate</textPath>
      </text>
    </svg>
  </section>

  <section class="screen screen--modern">
    <h1 class="modern-title">Still Lanterns</h1>
    <p class="modern-subtitle">Letters Written Beside a Quiet Harbor Gate</p>
    <svg class="cross-mark" width="44" height="46" viewBox="0 0 44 46">
      <line x1="22" y1="0" x2="22" y2="46" stroke="var(--gold)" stroke-width="1"/>
      <line x1="1" y1="11" x2="43" y2="11" stroke="var(--gold)" stroke-width="1"/>
    </svg>
    <p class="modern-dates">1 MARCH – 5 APRIL</p>
  </section>

</main>
</body>
</html>
```